Business card for psychiatrist

Business card design project for a psychiatristWe would like to have the impression of 1. We (patient and the doctor) are working together.2. Light the way so that patients can see where they are going and what their goals are.3. One side of the business card will have the letter "BFP" which stands for Brynmoor Family Psychiatry.4. The other side of the business card will have the address, phone number, name of the psychiatrist, website, etc.5. A logo could go into either side of the business card. Let's see what looks better.
Business card design project for a psychiatrist
We would like to have the impression of
1. We (patient and the doctor) are working together.
2. Light the way so that patients can see where they are going and what their goals are.
3. One side of the business card will have the letter "BFP" which stands for Brynmoor Family Psychiatry.
4. The other side of the business card will have the address, phone number, name of the psychiatrist, website, etc.
5. A logo could go into either side of the business card. Let's see what looks better.

```html
<!DOCTYPE html>
<html lang="en">
<head>
<meta charset="UTF-8">
<title>Brynmoor Family Psychiatry – Business Card</title>
<link rel="stylesheet" href="https://fonts.googleapis.com/css2?family=Work+Sans:wght@400;500;600&display=swap">
<style>
  :root {
    --backdrop: #1c1c1c;
    --card: #262626;
    --card-edge: #303030;
    --ink-soft: #bdbdbd;
    --ink: #e6e6e6;
    --ink-muted: #9a9a9a;
    --rule: #8a8a8a;
  }
  * { margin: 0; padding: 0; box-sizing: border-box; }
  html, body {
    width: 1200px;
    height: 900px;
    overflow: hidden;
    background: var(--backdrop);
    font-family: "Work Sans", Arial, sans-serif;
  }
  .canvas {
    width: 1200px;
    height: 900px;
    display: flex;
    flex-direction: column;
    align-items: center;
    justify-content: center;
    gap: 46px;
  }
  .card {
    width: 660px;
    height: 377px;
    background: var(--card);
    border: 1px solid var(--card-edge);
    position: relative;
  }
  .card-front {
    display: flex;
    align-items: center;
    justify-content: center;
  }
  .brand {
    display: flex;
    align-items: center;
    gap: 18px;
    color: var(--ink-soft);
    font-weight: 500;
  }
  .brand-square {
    flex: none;
    background: var(--ink-soft);
  }
  .card-front .brand-square {
    width: 22px;
    height: 22px;
  }
  .card-front .brand-name {
    font-size: 38px;
    line-height: 1.15;
    letter-spacing: 1px;
  }
  .card-back {
    display: flex;
    align-items: center;
    padding: 0 44px 0 40px;
  }
  .brand-block {
    width: 250px;
  }
  .card-back .brand {
    gap: 12px;
    align-items: flex-start;
  }
  .card-back .brand-square {
    width: 14px;
    height: 14px;
    margin-top: 9px;
  }
  .card-back .brand-name {
    font-size: 28px;
    line-height: 1.2;
    letter-spacing: 0.5px;
  }
  .divider {
    width: 1px;
    height: 180px;
    background: var(--rule);
    margin: 0 28px 0 18px;
  }
  .contact-block {
    color: var(--ink);
  }
  .person-name {
    font-size: 24px;
    font-weight: 500;
    letter-spacing: 2px;
    text-transform: uppercase;
  }
  .person-role {
    font-size: 16px;
    color: var(--ink-muted);
    margin-bottom: 18px;
  }
  .address {
    font-size: 17px;
    line-height: 1.35;
    letter-spacing: 0.5px;
    margin-bottom: 12px;
  }
  .contact-line {
    display: flex;
    align-items: center;
    gap: 9px;
    font-size: 17px;
    letter-spacing: 0.5px;
    line-height: 1.5;
  }
  .contact-line svg {
    width: 13px;
    height: 13px;
    flex: none;
  }
</style>
</head>
<body>
<main class="canvas">
  <section class="card card-front">
    <div class="brand">
      <span class="brand-square"></span>
      <span class="brand-name">Brynmoor<br>Family Psychiatry</span>
    </div>
  </section>

  <section class="card card-back">
    <div class="brand-block">
      <div class="brand">
        <span class="brand-square"></span>
        <span class="brand-name">Brynmoor<br>Family<br>Psychiatry</span>
      </div>
    </div>
    <div class="divider"></div>
    <div class="contact-block">
      <div class="person-name">Daniel Hartley</div>
      <div class="person-role">Director</div>
      <div class="address">1180 Willow Creek<br>Road Tampa, FL 33610</div>
      <div class="contact-line">
        <svg viewBox="0 0 16 16" aria-hidden="true"><path d="M3.5 1.5l2.5 0 1 3.5-1.6 1.2a8 8 0 0 0 4.4 4.4L11 9l3.5 1v2.5c0 .8-.7 1.5-1.5 1.5A11.5 11.5 0 0 1 2 3c0-.8.7-1.5 1.5-1.5z" fill="#e6e6e6"/></svg>
        <span>555-014-2276</span>
      </div>
      <div class="contact-line">
        <svg viewBox="0 0 16 16" aria-hidden="true"><rect x="1.5" y="3.5" width="13" height="9" fill="none" stroke="#e6e6e6" stroke-width="1.4"/><path d="M1.5 3.5L8 9l6.5-5.5" fill="none" stroke="#e6e6e6" stroke-width="1.4"/></svg>
        <span>info@brynmoorfamily.com</span>
      </div>
      <div class="contact-line">
        <svg viewBox="0 0 16 16" aria-hidden="true"><circle cx="8" cy="8" r="6.5" fill="none" stroke="#e6e6e6" stroke-width="1.3"/><ellipse cx="8" cy="8" rx="3" ry="6.5" fill="none" stroke="#e6e6e6" stroke-width="1.1"/><path d="M1.5 8h13" stroke="#e6e6e6" stroke-width="1.1"/></svg>
        <span>www.brynmoorfamily.com</span>
      </div>
    </div>
  </section>
</main>
</body>
</html>
```